Postcard Design

We are a full service lawn and landscape maintenance business. Employees are myself as owner-operator and
my son as operator and pesticide applicator and hardscape designer and builder along with myself as helper in the
hardscape. We have over 30 years experience and have operated as Doug's Yard Trimming for 23 years since 1993.
We are dependable and reasonably priced and hard working. My son is an excellent operator. We are full service year round. Spring cleanups, Summer all service, Fall cleanups and Winter snow removal.

Industry/Entity Type

Business

```html
<!DOCTYPE html>
<html lang="en">
<head>
<meta charset="utf-8">
<title>Doug's Yard Trimming – Postcard</title>
<link rel="stylesheet" href="https://fonts.googleapis.com/css2?family=Oswald:wght@400;600&family=Lato:wght@400;700&family=Open+Sans:wght@400;600&family=Roboto+Condensed:wght@400&display=swap">
<style>
  :root {
    --green: #4cb13b;
    --green-dark: #2f8f25;
    --ink: #3a3a3a;
    --charcoal: #2f2f31;
    --grey-text: #555;
    --stamp: #cfcfcf;
    --backdrop: #efece7;
    --grass-a: #7fbf4a;
    --grass-b: #3f8a2a;
    --sky: #9cc7ec;
  }
  html, body { margin: 0; padding: 0; }
  body {
    width: 825px; height: 1200px; overflow: hidden;
    background: var(--backdrop);
    position: relative;
    font-family: "Lato", sans-serif;
  }
  .card {
    position: absolute; left: 85px; width: 655px;
    background: #fff; overflow: hidden;
    box-shadow: 0 2px 6px rgba(0,0,0,.18);
  }
  .card--front { top: 153px; height: 424px;
    background: linear-gradient(180deg,#fff 0%,#f6f7f5 55%,#eaf2e2 88%,#fff 100%); }
  .card--back { top: 672px; height: 423px; }
  .abs { position: absolute; }
  .card svg { position: absolute; left: 0; top: 0; }

  /* front */
  .headline-band {
    left: 0; top: 0; width: 280px; height: 102px; background: var(--green);
    box-sizing: border-box; padding: 30px 0 0 26px;
    font-family: "Oswald", sans-serif; font-weight: 400; color: #fff;
    font-size: 16px; line-height: 26px; text-transform: uppercase;
    white-space: nowrap;
  }
  .rule-dark { left: 0; top: 106px; width: 280px; height: 10px; background: var(--charcoal); }
  .business-name {
    left: 37px; top: 142px; font-weight: 600; font-size: 17px; color: var(--grey-text);
    font-family: "Open Sans", sans-serif; white-space: nowrap;
  }
  .call-button {
    left: 28px; top: 180px; width: 208px; height: 32px; border-radius: 9px;
    background: linear-gradient(180deg,#66c94f,var(--green-dark));
    border: 2px solid #2e6d22; box-sizing: border-box;
    color: #fff; font-family: "Roboto Condensed", sans-serif; font-size: 19px;
    line-height: 28px; text-align: center; white-space: nowrap;
  }
  .inset-photo {
    left: 20px; top: 244px; width: 263px; height: 106px;
    border: 3px solid var(--green); box-sizing: border-box;
    background: linear-gradient(180deg,#8fcf5a 0%,#5aa236 60%,#3c7f27 100%);
  }
  .season-list {
    left: 308px; top: 266px; margin: 0; padding: 0; list-style: none;
    font-family: "Open Sans", sans-serif; font-size: 14px; line-height: 18.5px; color: var(--grey-text);
  }
  .season-list li::before {
    content: ""; display: inline-block; width: 6px; height: 6px; border-radius: 50%;
    background: var(--green); margin: 0 6px 2px 0;
  }
  .years { left: 488px; top: 266px; font-family: "Oswald", sans-serif; font-weight: 600;
    font-size: 21px; line-height: 1.3; color: var(--charcoal); white-space: nowrap; }
  .experience { left: 488px; top: 296px; font-family: "Oswald", sans-serif; font-weight: 600;
    font-size: 36px; line-height: 1; color: var(--green); letter-spacing: -.8px; white-space: nowrap; }
  .rule-green { left: 0; top: 367px; width: 655px; height: 4px; background: var(--green); }
  .footer {
    background: var(--charcoal); color: #fff; font-family: "Open Sans", sans-serif;
    white-space: nowrap;
  }
  .card--front .footer { left: 0; top: 374px; width: 655px; height: 50px;
    font-size: 15px; line-height: 50px; text-align: center; letter-spacing: 3.2px; }

  /* back */
  .back-panel { left: 0; top: 0; width: 330px; height: 423px;
    background: linear-gradient(180deg,#fff 0%,#f4f6f2 70%,#dcebcf 100%); }
  .stamp-box { left: 572px; top: 25px; width: 58px; height: 60px; background: var(--stamp); }
  .service-title { left: 23px; top: 247px; color: var(--green); font-weight: 700; font-size: 19px; }
  .service-list { left: 22px; top: 279px; margin: 0; padding: 0; list-style: none;
    font-size: 12px; line-height: 15.8px; color: var(--ink); width: 240px; }
  .service-list li { padding-left: 10px; text-indent: -10px; }
  .service-list li::before { content: "• "; }
  .card--back .footer { left: 0; top: 381px; width: 283px; height: 42px;
    font-size: 14px; line-height: 42px; padding-left: 26px; box-sizing: border-box; letter-spacing: 2px; }
  .address-area { left: 283px; top: 365px; width: 372px; height: 58px; background: #fff; }
</style>
</head>
<body>

<section class="card card--front">
  <svg width="655" height="372" viewBox="0 0 655 372">
    <defs>
      <linearGradient id="frontPhotoTone" x1="0" y1="0" x2="0" y2="1">
        <stop offset="0" stop-color="var(--sky)"/>
        <stop offset=".45" stop-color="#b9c3c2"/>
        <stop offset=".6" stop-color="#4d5a58"/>
        <stop offset=".8" stop-color="var(--grass-a)"/>
        <stop offset="1" stop-color="var(--grass-b)"/>
      </linearGradient>
    </defs>
    <path d="M345 0 C 290 60 262 150 255 220 C 380 186 520 222 655 182 L655 0 Z" fill="#fff"/>
    <path d="M352 0 C 300 60 274 140 266 210 C 390 178 520 210 655 172 L655 0 Z"
          fill="url(#frontPhotoTone)" role="img" aria-label="Photo of a lawn mower on freshly cut grass in front of suburban houses"/>
    <path d="M352 0 C 300 60 274 140 266 210" fill="none" stroke="var(--green)" stroke-width="4"/>
    <path d="M255 220 C 380 186 520 222 655 182" fill="none" stroke="var(--green)" stroke-width="5"/>
  </svg>

  <div class="abs headline-band">We are a full service lawn and<br>landscape maintenance business</div>
  <div class="abs rule-dark"></div>
  <div class="abs business-name">Doug's Yard Trimming</div>
  <div class="abs call-button">Call us at - 555.201.7788</div>
  <div class="abs inset-photo" role="img" aria-label="Photo of a blue push mower on green grass"></div>

  <ul class="abs season-list">
    <li>Spring cleanups</li>
    <li>Summer all service</li>
    <li>Fall cleanups</li>
    <li>Winter snow removal</li>
  </ul>
  <div class="abs years">Over 30 years</div>
  <div class="abs experience">Experience</div>

  <div class="abs rule-green"></div>
  <div class="abs footer">Please visit us to know more at – www.dougsyard.example</div>
</section>

<section class="card card--back">
  <div class="abs back-panel"></div>
  <svg width="655" height="423" viewBox="0 0 655 423">
    <defs>
      <linearGradient id="backPhotoTone" x1="0" y1="0" x2="1" y2="1">
        <stop offset="0" stop-color="#9fd46a"/>
        <stop offset=".5" stop-color="#6fba3c"/>
        <stop offset="1" stop-color="var(--grass-b)"/>
      </linearGradient>
    </defs>
    <path d="M280 0 C 330 40 370 110 366 180 C 372 260 345 320 318 366 L655 366 L655 0 Z" fill="#fff"/>
    <path d="M280 0 C 322 36 356 100 358 175 C 360 255 340 315 312 366" fill="none" stroke="var(--green)" stroke-width="6"/>
    <path d="M272 12 C 304 50 328 105 328 170 C 330 255 312 318 290 366" fill="none" stroke="var(--charcoal)" stroke-width="4"/>
    <path d="M0 0 L268 0 C 320 40 356 110 352 200 C 250 175 130 235 0 205 Z"
          fill="url(#backPhotoTone)" role="img" aria-label="Photo of a green lawn mower cutting grass"/>
    <path d="M0 205 C 130 235 250 175 362 205" fill="none" stroke="var(--green)" stroke-width="5"/>
    <path d="M268 0 C 320 40 356 110 352 200" fill="none" stroke="var(--green)" stroke-width="5"/>
  </svg>
  <div class="abs stamp-box"></div>

  <div class="abs service-title">Our Service:</div>
  <ul class="abs service-list">
    <li>Lorem ipsum dolor sit amet<br>Lorem ipsum dolor</li>
    <li>Lorem ipsum dolor sit amet lorem ipsum dolor sit amet lorem</li>
    <li>Lorem ipsum dolor sit amet</li>
    <li>Lorem ipsum dolor sit amet</li>
  </ul>

  <div class="abs address-area"></div>
  <div class="abs footer">www.dougsyard.example</div>
</section>

</body>
</html>
```